Skin Care Branding / Package design

We are a manufacturer of consumable hemp products and have some skin care products we want to group into a brand of its own, under our primary brand which is TulaMoss.  our website is www.tulamossgoods.example
Our current packaging was developed on the fly with little or no thought given to a sub brand concept.  We have sub branded other products such as Quiet Fern, Willow Crest, and Harbin.  While TulaMoss appears on the packaging it is not the predominate brand.
The products will be sold in cosmetic stores, health stores, medspas, pharmacies and other upscale stores.  We want the appeal to be elegant & upscale and stand out on the shelf.
We are open to changing the jar, bottle or container and look forward to any recommendations on this.
Later we will need flyers, social media ads, and other graphics.
Our primary goal is to create designs for each of our products that are consistent and create another sub brand.
We are also open to changing the names of these products.
images of the existing products are attached, we plan to add more skin care products.

```html
<!DOCTYPE html>
<html lang="en">
<head>
<meta charset="utf-8">
<title>TulaMoss Facial Serum – Carton Front Panel</title>
<link rel="stylesheet" href="https://fonts.googleapis.com/css2?family=Advent+Pro:wght@200;300&family=Work+Sans:wght@300;400&display=swap">
<style>
  :root {
    --stage: #efefed;
    --carton: #fbfbfa;
    --ink: #4a4a4c;
    --ink-soft: #626265;
    --rule: #8c8c8f;
    --brand-green: #3f9a3a;
    --wash-blush: #f1c7c6;
    --wash-rose: #ec7488;
    --wash-violet: #b98bd2;
    --wash-teal: #a9dccd;
  }
  * { margin: 0; padding: 0; box-sizing: border-box; }
  html, body { width: 1200px; height: 1200px; overflow: hidden; }
  body {
    background: var(--stage);
    font-family: "Work Sans", "Helvetica Neue", Arial, sans-serif;
    color: var(--ink);
  }
  .carton-front {
    position: absolute;
    left: 410px;
    top: 40px;
    width: 380px;
    height: 1120px;
    background: var(--carton);
    overflow: hidden;
    box-shadow: 0 2px 18px rgba(0,0,0,0.06);
  }
  .illustration-area {
    position: absolute;
    left: 0;
    top: 400px;
    width: 380px;
    height: 720px;
    background: linear-gradient(180deg,
      rgba(251,251,250,0) 0%,
      var(--wash-blush) 22%,
      var(--wash-rose) 50%,
      var(--wash-violet) 78%,
      var(--wash-teal) 100%);
  }
  .brand {
    position: absolute;
    left: 48px;
    top: 160px;
    display: flex;
    align-items: center;
    gap: 10px;
  }
  .brand-mark {
    width: 18px;
    height: 18px;
    background: var(--brand-green);
  }
  .brand-name {
    font-weight: 400;
    font-size: 22px;
    letter-spacing: 1px;
    color: var(--ink);
  }
  .product-name {
    position: absolute;
    left: 46px;
    top: 256px;
    font-family: "Advent Pro", "Arial Narrow", sans-serif;
    font-weight: 200;
    font-size: 78px;
    line-height: 0.9;
    color: var(--ink);
  }
  .product-purpose {
    position: absolute;
    left: 48px;
    top: 425px;
    font-weight: 300;
    font-size: 26px;
    letter-spacing: 1px;
    color: var(--ink);
  }
  .specs {
    position: absolute;
    left: 48px;
    top: 496px;
    width: 130px;
    color: var(--ink-soft);
  }
  .specs .infusion {
    font-size: 13px;
    font-weight: 300;
    letter-spacing: 0.4px;
    padding-bottom: 6px;
    border-bottom: 1.5px solid var(--rule);
  }
  .specs .strength {
    margin-top: 8px;
    font-size: 17px;
    font-weight: 300;
  }
  .specs .net-weight {
    margin-top: 4px;
    font-size: 12px;
    font-weight: 300;
  }
</style>
</head>
<body>
  <main class="carton-front">
    <div class="illustration-area" role="img" aria-label="Abstract watercolor wash in blush, rose, violet and soft teal covering the lower part of the panel"></div>

    <div class="brand">
      <span class="brand-mark"></span>
      <span class="brand-name">TulaMoss</span>
    </div>

    <h1 class="product-name">FACIAL<br>SERUM</h1>
    <p class="product-purpose">FOR BEAUTY</p>

    <div class="specs">
      <p class="infusion">CBD INFUSED</p>
      <p class="strength">300mg CBG</p>
      <p class="net-weight">net wt .5oz / 15g</p>
    </div>
  </main>
</body>
</html>
```